"MEET THE TEAM" page web design

We need a "meet the team" page for our website!
Please look at our website to see the style we need

We are looking for something unique, fun, cool, technology-style and yet professional. We plan on taking a picture of each employee (not sure if this will be a real photo/caricature/ black and white/goofy picture--> but we are open to any ideas you have that will work with the design) and putting it there, along with a little bio about each person.

Thanks! looking forward to working together:)
Updates

Project Deadline Extended
Reason: I am excited to see more designs and find the perfect fit. Thanks designers :)

Target Market(s)

People looking to purchase servers, workstations, components

Industry/Entity Type

Information Technology

Number of Pages Required

1 page

Font styles to use
Sans Serif
Other font styles liked:
• The font we use on our site so it matches

Requirements
Must have
• please look at our website qondimex.com and see the theme and colors we want.
• We have 13 employees but would like to have a design where we can add/remove people if we hire/terminate them without messing up the design.
• We are looking for something unique, fun, cool, technology-style and yet professional. We plan on taking a picture of each employee (not sure if this will be a real photo/caricature/ black and white/goofy picture--> but we are open to any ideas you have that will work with the design) and putting it there, along with a little bio about each person.
• We can upload anything you need
Nice to have
• We are also interested in having a design where when the cursor moves over a person then the bio comes out or moves around, or something. (This is not required, but we would love some cool ideas) And if you can come up with some design, we would have our programmers create it for us.
Should not have
• we are open to anything

```html
<!DOCTYPE html>
<html lang="en">
<head>
<meta charset="utf-8">
<title>Technical Team – Qondimex</title>
<link href="https://fonts.googleapis.com/css2?family=Raleway:wght@400;500;600&family=Arimo:wght@400;700&display=swap" rel="stylesheet">
<style>
:root{
  --teal:#1fa89d;
  --teal-light:#3fd0c2;
  --ink:#333;
  --muted:#666;
  --line:#d9d9d9;
  --footer:#a5a4a6;
  --footer-dark:#929193;
  --white:#fff;
}
*{margin:0;padding:0;box-sizing:border-box}
html,body{width:810px;height:1200px;overflow:hidden;background:var(--white);font-family:"Arimo",Arial,sans-serif;color:var(--ink)}
.page{position:relative;width:810px;height:1200px}
.abs{position:absolute}
.brand{left:44px;top:20px;display:flex;align-items:center;gap:10px}
.brand-dot{width:44px;height:44px;border-radius:50%;background:var(--teal)}
.brand-name{font-family:"Raleway",sans-serif;font-weight:500;font-size:24px;letter-spacing:3px;color:var(--teal)}
.account{left:638px;top:0;width:131px;height:22px;border-radius:0 0 12px 12px;background:#bdbdbd;display:flex;font-size:7px;color:#555}
.account span{flex:1;display:flex;align-items:center;justify-content:center}
.account span+span{background:#a9a9a9;border-radius:0 0 12px 0}
.contact-top{top:30px;display:flex;align-items:center;gap:6px}
.icon-circle{width:28px;height:28px;border-radius:50%;border:1px solid var(--line);display:flex;align-items:center;justify-content:center}
.live-chat{left:562px;font-size:9px;color:var(--muted)}
.phone-top{left:655px;font-size:13px;color:#444}
.nav{left:0;top:68px;width:810px;height:35px;border-top:1px solid var(--line);display:flex;align-items:center;padding-left:42px;gap:18px;font-family:"Raleway",sans-serif;font-size:7.5px;letter-spacing:.3px;color:#444}
.search{left:628px;top:76px;width:112px;height:22px;border:1px solid #ccc;border-radius:11px;font-size:7.5px;padding:6px 14px;color:#444}
.cart{left:746px;top:74px;width:26px;height:26px}
.crumb{left:0;top:103px;width:810px;height:25px;background:linear-gradient(90deg,#1ea79d,#3fd6c5 50%,#24a99e);font-size:8px;font-weight:700;color:var(--white);padding:8px 0 0 88px}
.crumb b{color:#17443f}
.side{left:42px;top:158px;width:130px;height:116px;border:1px solid var(--line)}
.side h2{background:var(--teal);color:var(--white);font-family:"Raleway",sans-serif;font-weight:500;font-size:11px;height:25px;padding:7px 0 0 11px}
.side ul{list-style:none;padding:8px 0 0 15px;font-size:8px;color:var(--teal)}
.side li{height:19px;padding:3px 9px}
.side li.active{background:var(--teal);color:var(--white);width:101px}
.main{left:211px;top:159px;width:560px;height:662px;border:2px solid #e2e2e2}
.main h1{position:absolute;left:25px;top:14px;font-family:"Raleway",sans-serif;font-weight:500;font-size:15px;color:var(--teal)}
.card{width:132px;height:262px;border:2px solid #e2e2e2;background:var(--white)}
.photo{height:130px;background:linear-gradient(160deg,#cfcfcf,#8a8a8a)}
.photo.warm{background:linear-gradient(160deg,#c9a48a,#6e4c3a)}
.bio{height:130px;background:var(--teal);color:var(--white);font-size:8.4px;line-height:12.5px;padding:10px 9px}
.bio p+p{margin-top:9px}
.name{text-align:center;font-family:"Raleway",sans-serif;font-size:11.5px;color:var(--teal);margin-top:10px}
.role{text-align:center;font-size:8.5px;margin-top:5px}
.rule{height:1px;background:var(--line);margin:8px 10px}
.row{display:flex;align-items:center;gap:6px;font-size:7.4px;padding-left:7px;height:18px}
.socials{display:flex;justify-content:center;gap:14px;margin-top:10px}
.socials span{width:12px;height:12px;background:#111;border-radius:2px}
.footer{left:0;top:869px;width:810px;height:212px;background:var(--footer);color:var(--white)}
.footer-text{width:356px;margin:14px auto 0;text-align:center;font-size:10px;line-height:13px}
.footer-rule{width:490px;height:1px;background:#bdbdbd;margin:6px auto 0}
.footer-contact{position:absolute;top:101px;font-size:10px;line-height:14px;display:flex;align-items:flex-start;gap:7px}
.footer-contact svg{margin-top:2px}
.footer-links{position:absolute;top:143px;display:flex;font-size:11.5px;font-family:"Raleway",sans-serif}
.support{position:absolute;left:527px;top:162px;text-align:center;font-size:6.5px;line-height:9.5px;font-weight:700;width:70px}
.bottom{left:0;top:1081px;width:810px;height:119px;background:var(--footer-dark);color:var(--white)}
.circles{display:flex;justify-content:center;gap:10px;margin-top:14px}
.circles span{width:26px;height:26px;border:1px solid #c8c8c8;border-radius:50%}
.bottom-rule{width:580px;height:1px;background:#bdbdbd;margin:14px auto 0}
.copy{display:flex;justify-content:center;align-items:center;gap:8px;margin-top:10px;font-size:9px;line-height:12px}
.copy-dot{width:14px;height:14px;border-radius:50%;background:#ddd}
</style>
</head>
<body>
<div class="page">
  <div class="abs brand"><span class="brand-dot"></span><span class="brand-name">QONDIMEX</span></div>
  <div class="abs account"><span>SIGN UP</span><span>LOGIN</span></div>
  <div class="abs contact-top live-chat"><span class="icon-circle"><svg width="12" height="10" viewBox="0 0 12 10"><path d="M1 1h8v5H4l-3 2z" fill="var(--teal)"/></svg></span>LIVE CHAT</div>
  <div class="abs contact-top phone-top"><span class="icon-circle"><svg width="12" height="12" viewBox="0 0 12 12"><path d="M2 1l2 0 1 3-1.5 1a7 7 0 0 0 3.5 3.5L8 7l3 1v2a1 1 0 0 1-1 1A9 9 0 0 1 1 2a1 1 0 0 1 1-1z" fill="var(--teal)"/></svg></span>555-014-2270</div>

  <nav class="abs nav"><span>SERVERS</span><span>WORKSTATIONS</span><span>COMPONENTS</span><span>VIRTUAL REALITY</span><span>DRONES</span><span>ABOUT US</span><span>BLOG</span><span>RESOURCES</span><span>CONTACT US</span></nav>
  <div class="abs search">Search</div>
  <svg class="abs" style="left:718px;top:81px" width="11" height="11" viewBox="0 0 11 11"><circle cx="4.5" cy="4.5" r="3.5" fill="none" stroke="var(--teal)" stroke-width="1.6"/><path d="M7 7l3 3" stroke="var(--teal)" stroke-width="1.6"/></svg>
  <svg class="abs cart" viewBox="0 0 26 26"><circle cx="13" cy="13" r="12" fill="#fff" stroke="#ccc"/><rect x="7" y="10" width="12" height="7" rx="1" fill="var(--teal)"/><rect x="9" y="8" width="8" height="2" fill="var(--teal)"/></svg>

  <div class="abs crumb">HOME / <b>TEAM MEMBER</b></div>

  <aside class="abs side">
    <h2>TEAM MEMBER</h2>
    <ul><li>Management Team</li><li class="active">Technical Team</li><li>Sales Team</li><li>Marketing Team</li></ul>
  </aside>

  <section class="abs main">
    <h1>Technical Team</h1>
  </section>

  <div class="abs" style="left:237px;top:207px">
    <article class="card">
      <div class="bio"><p>Lorem ipsum dolor sit amet, consectetur adipiscing elit, sed do eiusmod tempor incididunt ut labore et dolore magna aliqua.</p><p>Lorem ipsum dolor sit amet, consectetur adipiscing elit, sed do eiusmod</p></div>
      <div class="name">Arjun Mehta</div><div class="role">Chairman</div><div class="rule"></div>
      <div class="row"><svg width="10" height="10" viewBox="0 0 12 12"><path d="M2 1l2 0 1 3-1.5 1a7 7 0 0 0 3.5 3.5L8 7l3 1v2a1 1 0 0 1-1 1A9 9 0 0 1 1 2a1 1 0 0 1 1-1z"/></svg>+91 5550 1234 56</div>
      <div class="row"><svg width="11" height="8" viewBox="0 0 11 8"><rect x=".5" y=".5" width="10" height="7" fill="none" stroke="#111"/><path d="M.5.5l5 4 5-4" fill="none" stroke="#111"/></svg>arjun.team@mailbox.test</div>
      <div class="rule"></div><div class="socials"><span></span><span></span><span></span><span></span></div>
    </article>
  </div>
  <div class="abs" style="left:429px;top:207px">
    <article class="card">
      <div class="photo" role="img" aria-label="Portrait photo of team member"></div>
      <div class="name">Arjun Mehta</div><div class="role">Chairman</div><div class="rule"></div>
      <div class="row"><svg width="10" height="10" viewBox="0 0 12 12"><path d="M2 1l2 0 1 3-1.5 1a7 7 0 0 0 3.5 3.5L8 7l3 1v2a1 1 0 0 1-1 1A9 9 0 0 1 1 2a1 1 0 0 1 1-1z"/></svg>+91 5550 1234 56</div>
      <div class="row"><svg width="11" height="8" viewBox="0 0 11 8"><rect x=".5" y=".5" width="10" height="7" fill="none" stroke="#111"/><path d="M.5.5l5 4 5-4" fill="none" stroke="#111"/></svg>arjun.team@mailbox.test</div>
      <div class="rule"></div><div class="socials"><span></span><span></span><span></span><span></span></div>
    </article>
  </div>
  <div class="abs" style="left:611px;top:207px">
    <article class="card">
      <div class="photo warm" role="img" aria-label="Portrait photo of team member"></div>
      <div class="name">Arjun Mehta</div><div class="role">Chairman</div><div class="rule"></div>
      <div class="row"><svg width="10" height="10" viewBox="0 0 12 12"><path d="M2 1l2 0 1 3-1.5 1a7 7 0 0 0 3.5 3.5L8 7l3 1v2a1 1 0 0 1-1 1A9 9 0 0 1 1 2a1 1 0 0 1 1-1z"/></svg>+91 5550 1234 56</div>
      <div class="row"><svg width="11" height="8" viewBox="0 0 11 8"><rect x=".5" y=".5" width="10" height="7" fill="none" stroke="#111"/><path d="M.5.5l5 4 5-4" fill="none" stroke="#111"/></svg>arjun.team@mailbox.test</div>
      <div class="rule"></div><div class="socials"><span></span><span></span><span></span><span></span></div>
    </article>
  </div>
  <div class="abs" style="left:237px;top:515px">
    <article class="card">
      <div class="photo" role="img" aria-label="Portrait photo of team member"></div>
      <div class="name">Arjun Mehta</div><div class="role">Chairman</div><div class="rule"></div>
      <div class="row"><svg width="10" height="10" viewBox="0 0 12 12"><path d="M2 1l2 0 1 3-1.5 1a7 7 0 0 0 3.5 3.5L8 7l3 1v2a1 1 0 0 1-1 1A9 9 0 0 1 1 2a1 1 0 0 1 1-1z"/></svg>+91 5550 1234 56</div>
      <div class="row"><svg width="11" height="8" viewBox="0 0 11 8"><rect x=".5" y=".5" width="10" height="7" fill="none" stroke="#111"/><path d="M.5.5l5 4 5-4" fill="none" stroke="#111"/></svg>arjun.team@mailbox.test</div>
      <div class="rule"></div><div class="socials"><span></span><span></span><span></span><span></span></div>
    </article>
  </div>
  <div class="abs" style="left:429px;top:515px">
    <article class="card">
      <div class="photo" role="img" aria-label="Portrait photo of team member"></div>
      <div class="name">Arjun Mehta</div><div class="role">Chairman</div><div class="rule"></div>
      <div class="row"><svg width="10" height="10" viewBox="0 0 12 12"><path d="M2 1l2 0 1 3-1.5 1a7 7 0 0 0 3.5 3.5L8 7l3 1v2a1 1 0 0 1-1 1A9 9 0 0 1 1 2a1 1 0 0 1 1-1z"/></svg>+91 5550 1234 56</div>
      <div class="row"><svg width="11" height="8" viewBox="0 0 11 8"><rect x=".5" y=".5" width="10" height="7" fill="none" stroke="#111"/><path d="M.5.5l5 4 5-4" fill="none" stroke="#111"/></svg>arjun.team@mailbox.test</div>
      <div class="rule"></div><div class="socials"><span></span><span></span><span></span><span></span></div>
    </article>
  </div>
  <div class="abs" style="left:611px;top:515px">
    <article class="card">
      <div class="photo warm" role="img" aria-label="Portrait photo of team member"></div>
      <div class="name">Arjun Mehta</div><div class="role">Chairman</div><div class="rule"></div>
      <div class="row"><svg width="10" height="10" viewBox="0 0 12 12"><path d="M2 1l2 0 1 3-1.5 1a7 7 0 0 0 3.5 3.5L8 7l3 1v2a1 1 0 0 1-1 1A9 9 0 0 1 1 2a1 1 0 0 1 1-1z"/></svg>+91 5550 1234 56</div>
      <div class="row"><svg width="11" height="8" viewBox="0 0 11 8"><rect x=".5" y=".5" width="10" height="7" fill="none" stroke="#111"/><path d="M.5.5l5 4 5-4" fill="none" stroke="#111"/></svg>arjun.team@mailbox.test</div>
      <div class="rule"></div><div class="socials"><span></span><span></span><span></span><span></span></div>
    </article>
  </div>

  <footer class="abs footer">
    <p class="footer-text">Based in Westmere California, Qondimex offers custom servers, storage, and workstations for local businesses in Los Angeles, Beverly Hills, Thousand Oaks, Ventura, Orange County, Santa Barbara, Oxnard, Irvine, Anaheim, and San Diego. Qondimex also offers such products to clients throughout the United States and Worldwide.</p>
    <div class="footer-rule"></div>
    <div class="footer-contact" style="left:245px"><svg width="8" height="11" viewBox="0 0 8 11"><path d="M4 0a4 4 0 0 1 4 4c0 3-4 7-4 7S0 7 0 4a4 4 0 0 1 4-4z" fill="#fff"/><circle cx="4" cy="4" r="1.5" fill="var(--footer)"/></svg><span>4820 Orlin Ave.<br>Westmere, CA 91400</span></div>
    <div class="footer-contact" style="left:368px"><svg width="10" height="10" viewBox="0 0 12 12"><path d="M2 1l2 0 1 3-1.5 1a7 7 0 0 0 3.5 3.5L8 7l3 1v2a1 1 0 0 1-1 1A9 9 0 0 1 1 2a1 1 0 0 1 1-1z" fill="#fff"/></svg><span>555-014-2270</span></div>
    <div class="footer-contact" style="left:478px"><svg width="11" height="8" viewBox="0 0 11 8"><rect width="11" height="8" fill="#fff"/><path d="M0 0l5.5 4L11 0" fill="none" stroke="var(--footer)"/></svg><span>sales@qondimex.com</span></div>
    <div class="footer-links" style="left:223px">Hardware</div>
    <div class="footer-links" style="left:315px">Drones</div>
    <div class="footer-links" style="left:381px">Reality</div>
    <div class="footer-links" style="left:456px">About</div>
    <div class="footer-links" style="left:516px">Customer Support</div>
    <div class="support">Terms and<br>Conditions<br>Warranty Information<br>Contact Us<br>Return Policy</div>
  </footer>

  <div class="abs bottom">
    <div class="circles"><span></span><span></span><span></span><span></span></div>
    <div class="bottom-rule"></div>
    <div class="copy"><span class="copy-dot"></span><span>Qondimex, LLC.<br>Copyright © 2017</span></div>
  </div>
</div>
</body>
</html>
```